2018 Vision Board Workshop

I need to promote this workshop on both an 8.5x11 sheet and a 5x7 card. I do have a logo that needs to be present. I'd like to stay true to my branded colors. The flyer needs to project the excitement of a new year and the possibilities of what a person can create, produce, explore in their lives by putting it all on a vision board. Creating the vision of what you want will inspire you to achieve your goals and dreams. Looking at your vision board each day will propel you into taking action as you chart your course to achieve what you truly want.
The flyer needs to have the following information:
The workshop date and time - Sat., Jan. 13, 2018, 10:30-1:30
The location is - Atrium 47B, 2864 Birchwood Vale Rd, Colorado Springs, Co 80417
in the FORGE Room
My name and contact information - Mara Vollbeck
Text and voice 303-417-6652
Email - mara@brightwell-daily-craft.com
Website - brightwell-daily-craft.com
The fee is $45. All materials are provided.

My company is called Brightwell Daily Craft. I am a Life Coach, author, speaker and workshop leader.\ I wrote this program, Brightwell Daily Craft to teach concepts and supporting skills for living with more happiness, satisfaction and fulfillment. Thanks for reading this!! Mara

Target Market(s)

Primarily women, educated, motivated, proactive in their own lives and well being

Font styles to use
Other font styles liked:
• I have been using Century Gothic. I'm open to new ideas.

Requirements
Must have
• The Brightwell Daily Craft logo
• The flyer needs to have the following information:
• The workshop date and time - Sat., Jan. 13, 2018, 10:30-1:30
• The location is - Atrium 47B, 2864 Birchwood Vale Rd, Colorado Springs, Co 80417
• in the FORGE Room
• My name and contact information - Mara Vollbeck
• Text and voice 303-417-6652
• Email - mara@brightwell-daily-craft.com
• Website - brightwell-daily-craft.com
• The fee is $45. All materials are provided.
Nice to have
• The Brightwell Daily Craft branded colors in the design
• Images of vision boards

```html
<!DOCTYPE html>
<html lang="en">
<head>
<meta charset="utf-8">
<title>2018 Vision Board Workshop — Brightwell Daily Craft</title>
<link rel="stylesheet" href="https://fonts.googleapis.com/css2?family=Questrial&family=Nunito:wght@700;800&display=swap">
<style>
  :root {
    --brand-blue: #4aa8de;
    --brand-blue-deep: #3b8fd0;
    --brand-green: #9dcb3c;
    --white: #ffffff;
    --paper: #fbfbfb;
  }
  * { margin: 0; padding: 0; box-sizing: border-box; }
  html, body { width: 1200px; height: 857px; overflow: hidden; background: var(--white); }
  .flyer {
    position: relative; width: 1200px; height: 857px; overflow: hidden;
    font-family: "Questrial", "Century Gothic", sans-serif;
    background: linear-gradient(180deg, var(--white) 0%, var(--paper) 70%);
  }
  .stationery-backdrop {
    position: absolute; left: 0; right: 0; bottom: 0; height: 260px;
    background:
      radial-gradient(ellipse 180px 60px at 170px 200px, rgba(120,120,120,.35), transparent 70%),
      radial-gradient(ellipse 120px 50px at 480px 160px, rgba(240,150,140,.25), transparent 70%),
      radial-gradient(ellipse 160px 70px at 760px 90px, rgba(210,235,150,.4), transparent 70%),
      radial-gradient(ellipse 140px 60px at 1000px 90px, rgba(250,215,160,.35), transparent 70%),
      radial-gradient(ellipse 120px 60px at 1000px 240px, rgba(240,170,200,.35), transparent 70%),
      linear-gradient(180deg, rgba(255,255,255,0) 0%, rgba(240,240,236,.7) 100%);
  }

  /* Brand wordmark */
  .brand { position: absolute; left: 70px; top: 168px; width: 500px; text-align: center; }
  .brand-name { color: var(--brand-green); font-size: 44px; letter-spacing: .5px; line-height: 1; white-space: nowrap; }
  .brand-tagline { color: var(--brand-blue-deep); font-size: 19px; letter-spacing: 1px; margin-top: 16px; padding-left: 130px; text-align: left; }

  /* Host */
  .host-portrait {
    position: absolute; left: 54px; top: 276px; width: 180px; height: 180px; border-radius: 50%;
    border: 6px solid var(--brand-blue);
    background: radial-gradient(circle at 50% 40%, #f1d3b5 0%, #d9a25a 45%, #b4762c 75%, #7aa7a0 100%);
    z-index: 2;
  }
  .host-band {
    position: absolute; left: 200px; top: 302px; width: 384px; height: 60px;
    background: var(--brand-blue);
    clip-path: polygon(0 0, 372px 0, 384px 60px, 0 60px);
  }
  .host-name { position: absolute; left: 264px; top: 308px; color: var(--white); font-size: 39px; line-height: 48px; }
  .host-roles { position: absolute; left: 267px; top: 372px; color: var(--brand-green); font-size: 27px; line-height: 45px; }

  /* Contact bands */
  .contact {
    position: absolute; left: 0; width: 602px; height: 38px; background: var(--brand-blue);
    clip-path: polygon(0 0, 588px 0, 602px 38px, 0 38px);
    color: var(--white); font-size: 26px; line-height: 38px; text-align: right; padding-right: 30px;
  }
  .contact--phone { top: 500px; padding-right: 32px; }
  .contact--email { top: 569px; padding-right: 18px; }
  .contact--web { top: 645px; padding-right: 18px; }

  /* Event details */
  .event-panel { position: absolute; left: 0; top: 0; }
  .date-band { position: absolute; left: 632px; top: 76px; color: var(--white); font-size: 41px; line-height: 50px; white-space: nowrap; }
  .details { position: absolute; left: 672px; top: 180px; color: var(--white); font-size: 33px; line-height: 42px; }
  .details strong { font-family: "Nunito", "Century Gothic", sans-serif; font-weight: 800; }
  .fee {
    position: absolute; left: 752px; top: 512px; width: 270px; text-align: center;
    transform: rotate(-7deg);
    font-family: "Nunito", "Century Gothic", sans-serif; font-weight: 800; font-size: 37px; line-height: 42px;
    color: var(--brand-blue-deep);
  }
  .fee-amount { color: var(--brand-green); }

  .materials {
    position: absolute; left: 624px; top: 740px; width: 536px; height: 64px;
    background: rgba(255,255,255,.85);
    color: var(--brand-blue-deep); font-size: 35px; line-height: 64px; text-align: center;
  }
</style>
</head>
<body>
<main class="flyer">
  <div class="stationery-backdrop" role="img" aria-label="Soft photo of desk stationery: markers, paper clips, sticky notes and watercolours"></div>

  <header class="brand">
    <div class="brand-name">Brightwell Daily Craft</div>
    <div class="brand-tagline">What you think is what you create</div>
  </header>

  <section class="host">
    <div class="host-band"></div>
    <div class="host-portrait" role="img" aria-label="Portrait photo of workshop leader Mara Vollbeck"></div>
    <h1 class="host-name">Mara Vollbeck</h1>
    <p class="host-roles">Author, Coach, Speaker<br>and Workshop Leader</p>
  </section>

  <section class="contacts">
    <div class="contact contact--phone">Text and voice 303-417-6652</div>
    <div class="contact contact--email">Email - mara@brightwell-daily-craft.com</div>
    <div class="contact contact--web">Website - brightwell-daily-craft.com</div>
  </section>

  <svg class="event-panel" width="1200" height="857" viewBox="0 0 1200 857" aria-hidden="true">
    <path d="M650 134 H1120 V552 Q1120 648 885 648 Q650 648 650 552 Z" fill="var(--brand-green)"/>
    <polygon points="608,70 1136,70 1150,134 620,134" fill="var(--brand-blue)"/>
    <ellipse cx="884" cy="557" rx="189" ry="82" fill="var(--white)"/>
  </svg>

  <div class="date-band">Date : Sat., Jan. 13. 2018</div>
  <div class="details">
    <strong>Time:</strong> 10:30-1:30<br>
    <strong>Location:</strong> Atrium 47B,<br>
    2864 Birchwood Vale Rd,<br>
    Colorado Springs,<br>
    Co 80417<br>
    in the FORGE Room
  </div>
  <div class="fee">Registration<br>Fee: <span class="fee-amount">$45</span></div>

  <div class="materials">All materials are provided</div>
</main>
</body>
</html>
```